Expanding National Maid Service Needs Redesign!

We need a redesigned home page for our residential cleaning company. Winner will be recognized as the designer for a brand about to go national within the United States. Winner will also become the first choice to continue working with the company to design at least 15 more pages.

Looking for redesign of homepage and redesign of logo (logo will use the same elements -- just organized differently with horizontal text).

For the design we are looking for a mix between the following websites:
www. brigadeofsweepers .com
This is our parent site that will be redesigned

www. tidycorsairs .com
We really like the top/header having the three steps.
We would like to have the same font (proxima nova) and colors. We like the location and size of the booking form.
Love the section topics and would like to mimic that.

www. brighthavenkeepers .com
We really like the clean art and use of colors.
We love the use of b-roll and branded images. Will provide for our website.

The perfect site would have the cleanliness, layout and booking form of Tidy Corsairs and the excellent placement and use of branded images and b-roll of Bright Haven Keepers.

Link to branded images and b-roll is attached to the brief in a text file.

Please message me any questions. Good luck to everyone in the project!

Target Market(s)

Male and Female working professionals between the ages of 30-60 years old.

Industry/Entity Type

Cleaning Service

Number of Pages Required

1 page

Font styles to use
Other font styles liked:
• Proxima Nova

Colors
0355a3
add136

Requirements
Must have
• Most of this is covered in the project description.
• Would like to have our logo split up so that the art of the maids remains the same but the "Brigade of Sweepers" text is to the right of the art. Looking for it to be a horizontal logo.
• Must use Proxima Nova font.
• Must use our branded images and videos. Feel free to create stills from the video.
Nice to have
• Nice to have, but not expected, is the b-roll edited to work with your design. We would like to see the designers vision of how the video would look with the website.
• Would be nice to have our logo given an updated look. Made horizontal as mentioned in the project description.
Should not have
• Should not feel busy. Should not use different color scheme than that of Tidy Corsairs. Should not have non-branded images of maids.

```html
<!DOCTYPE html>
<html lang="en">
<head>
<meta charset="utf-8">
<title>Brigade of Sweepers – Home Cleaning</title>
<link href="https://fonts.googleapis.com/css2?family=Figtree:ital,wght@0,400;0,600;0,700;1,400&display=swap" rel="stylesheet">
<style>
:root{
  --sky:#1badea;
  --sky-dark:#0a95d1;
  --green:#3fb549;
  --green-dark:#2f9a3a;
  --ink:#2b2b2b;
  --muted:#6d6d6d;
  --line:#dedede;
  --paper:#ffffff;
  --mist:#f3f3f3;
  --star:#e8262b;
  --charcoal:#4a4a4a;
}
*{box-sizing:border-box;margin:0;padding:0}
html,body{width:1200px;height:3180px;overflow:hidden}
body{font-family:"Figtree",Arial,sans-serif;color:var(--ink);background:var(--paper);position:relative}
section,header,footer{position:relative;width:1200px}

/* header */
.site-header{height:142px}
.brand{position:absolute;left:18px;top:34px;display:flex;align-items:center;gap:12px}
.brand-dot{width:46px;height:46px;border-radius:50%;background:var(--green)}
.brand-name{font-size:34px;font-weight:700;color:var(--green)}
.login{position:absolute;right:28px;top:10px;background:var(--sky);color:#fff;font-size:26px;padding:6px 20px;border-radius:10px}
.main-nav{position:absolute;right:28px;top:70px;font-size:23px;color:#444;display:flex;gap:10px}
.main-nav .sep{color:#888}
.main-nav .phone{color:var(--sky-dark)}

/* steps */
.steps{height:38px;border-top:1px solid var(--line);border-bottom:1px solid var(--line)}
.steps svg{position:absolute;left:0;top:0}
.step{position:absolute;top:5px;font-size:15px;color:var(--sky);display:flex;align-items:center;gap:10px}
.step .num{width:25px;height:25px;border:2px solid var(--sky);border-radius:50%;display:flex;align-items:center;justify-content:center;font-size:14px}
.step.active{color:#fff}
.step.active .num{border-color:#fff}

/* hero */
.hero{height:706px;overflow:hidden}
.hero-photo{position:absolute;inset:0;background:linear-gradient(120deg,#d9dcd8 0%,#eceae6 40%,#c9d3cf 70%,#e6e2dc 100%)}
.hero-veil{position:absolute;inset:0;background:rgba(255,255,255,.55)}
.hero-title{position:absolute;left:36px;top:68px;font-size:38px;font-weight:400}
.hero-lead{position:absolute;left:36px;top:280px;font-size:22px}
.checks{position:absolute;left:36px;top:330px;list-style:none}
.checks li{font-size:22px;display:flex;align-items:center;gap:18px;height:54px}
.checks svg{flex:none}

.quote-form{position:absolute;left:906px;top:42px;width:240px;height:630px;background:#fff;border:1px solid #ddd;box-shadow:0 2px 8px rgba(0,0,0,.12);padding:22px 18px;text-align:center;font-size:12px;color:#444}
.quote-form h2{font-size:17px;font-weight:400;margin-bottom:14px}
.field{height:34px;border:1px solid #ccc;border-radius:3px;text-align:left;padding:9px 10px;color:#999;font-size:12px;margin-bottom:22px}
.label{margin:8px 0 10px}
.toggle{display:flex;height:34px;margin-bottom:16px}
.toggle span{flex:1;display:flex;align-items:center;justify-content:center;border:1px solid #ccc}
.toggle .on{background:var(--sky);color:#fff;border-color:var(--sky)}
.stepper{display:flex;height:34px;border:1px solid #ccc;border-radius:3px}
.stepper span{display:flex;align-items:center;justify-content:center}
.stepper .btn{width:30px;color:#666}
.stepper .val{flex:1;border-left:1px solid #ccc;border-right:1px solid #ccc}
.hint{font-size:9px;color:#999;margin:5px 0 18px}
.times{display:flex;align-items:center;gap:8px;margin-bottom:12px}
.times .field{flex:1;margin:0;color:#444;text-align:center;padding:9px 4px}
.flex-check{display:flex;justify-content:center;align-items:center;gap:6px;margin-bottom:20px}
.flex-check i{width:12px;height:12px;border:1px solid #888;display:inline-block;font-style:normal;font-size:10px;line-height:10px}
.cta{display:flex;align-items:center;justify-content:center;height:50px;background:var(--green);color:#fff;font-size:15px;border-radius:2px}

/* about */
.about{height:577px;text-align:center}
.section-title{font-size:38px;font-weight:400}
.about .section-title{padding-top:34px}
.about p{text-align:left;font-size:19px;line-height:33px;padding:0 36px}
.about .intro{margin-top:26px}
.circles{position:relative;height:250px}
.circle{position:absolute;top:42px;width:192px;height:192px;border-radius:50%}
.about .contact{margin-top:8px}
.learn{display:block;text-align:left;padding-left:36px;margin-top:14px;color:var(--green-dark);font-size:19px}

/* reviews */
.reviews{height:430px;background:var(--mist);text-align:center}
.reviews .section-title{padding-top:18px}
.reviews .sub{font-size:22px;color:#555;margin-top:12px}
.review{position:absolute;top:132px;width:330px;height:250px;background:#fff;padding:28px 36px 0;box-shadow:0 1px 3px rgba(0,0,0,.08)}
.review::after{content:"";position:absolute;left:120px;bottom:-14px;border:14px solid transparent;border-bottom:0;border-top-color:#fff}
.review q{display:block;font-style:italic;font-size:14px;line-height:22px;color:#555;text-align:justify;height:150px}
.review .who{font-size:11px;letter-spacing:1px;color:#555;margin-top:8px}
.stars{display:flex;gap:3px;justify-content:center;margin-top:12px}
.stars span{width:20px;height:20px;background:var(--star);display:flex;align-items:center;justify-content:center}

/* services */
.services{height:407px;text-align:center}
.services .section-title{padding-top:26px;font-size:35px}
.tile{position:absolute;top:110px;width:284px;text-align:center}
.tile .shot{height:148px}
.tile p{font-size:20px;margin-top:12px}
.services .note{position:absolute;left:0;right:0;top:354px;font-size:21px;color:#444}

/* area */
.area{height:399px;overflow:hidden;color:#fff}
.area-bg{position:absolute;inset:0;background:linear-gradient(90deg,#27b2ea,#4ec1ef 50%,#22aee8)}
.area .section-title{position:relative;text-align:center;padding-top:22px;font-size:36px}
.cities{position:absolute;top:100px;list-style:none;font-size:21px}
.cities li{height:40px;display:flex;align-items:center;gap:14px}
.cities li::before{content:"";width:7px;height:7px;border-radius:50%;background:#fff}
.schedule{position:absolute;left:436px;top:346px;width:256px;height:42px;background:#fff;color:#333;border-radius:22px;font-size:21px;display:flex;align-items:center;justify-content:center}

/* press */
.press{height:199px;text-align:center}
.press .section-title{padding-top:24px;font-size:35px}
.outlets{display:flex;justify-content:center;gap:44px;margin-top:40px;font-size:32px;color:#4b4b4b;font-weight:600}

/* footer */
.site-footer{height:208px;background:var(--sky);color:#fff}
.foot-brand{position:absolute;left:26px;top:44px;display:flex;align-items:center;gap:12px}
.foot-brand .brand-dot{background:#fff}
.foot-brand .brand-name{color:#fff}
.copy{position:absolute;left:18px;top:156px;font-size:14px}
.foot-links{position:absolute;top:54px;list-style:none;font-size:21px}
.foot-links li{height:40px}
.connect{position:absolute;left:912px;top:42px;font-size:16px}
.icons{display:flex;gap:10px;margin:8px 0 14px}
.icons span{width:34px;height:34px;border-radius:50%;background:#1d4a73}
.cards{display:flex;gap:6px;margin-top:8px}
.cards span{width:38px;height:24px;background:#fff;border-radius:2px}

.callbar{height:74px;background:var(--charcoal);color:#fff;font-size:28px;display:flex;align-items:center;justify-content:center}
</style>
</head>
<body>

<header class="site-header">
  <div class="brand"><span class="brand-dot"></span><span class="brand-name">Brigade of Sweepers</span></div>
  <span class="login">Log In</span>
  <nav class="main-nav">
    <span>Services &amp; Pricing</span><span class="sep">|</span><span>Gift Cards</span><span class="sep">|</span><span>About</span><span class="sep">|</span><span>Charity</span><span class="sep">|</span><span class="phone">(844) 555-0176</span>
  </nav>
</header>

<section class="steps">
  <svg width="420" height="38" viewBox="0 0 420 38"><polygon points="0,0 400,0 418,19 400,38 0,38" fill="var(--sky)"/></svg>
  <div class="step active" style="left:172px"><span class="num">1</span>Cleaning</div>
  <div class="step" style="left:494px"><span class="num">2</span>Pricing/Availability</div>
  <div class="step" style="left:890px"><span class="num">3</span>Done!</div>
</section>

<section class="hero">
  <div class="hero-photo" role="img" aria-label="Bright kitchen with a maid and a child at a table of fresh fruit"></div>
  <div class="hero-veil"></div>
  <h1 class="hero-title">Love that feeling of a fresh, clean home?</h1>
  <p class="hero-lead">Brigade of Sweepers Fighting the war on dirt with eco-friendly weapons.</p>
  <ul class="checks">
    <li><svg width="18" height="14" viewBox="0 0 18 14"><path d="M1 7l5 5L17 1" fill="none" stroke="var(--green)" stroke-width="3"/></svg>Your friends and family will love how clean you home looks and smells!</li>
    <li><svg width="18" height="14" viewBox="0 0 18 14"><path d="M1 7l5 5L17 1" fill="none" stroke="var(--green)" stroke-width="3"/></svg>Let us handle the cleaning so you can have more free time.</li>
    <li><svg width="18" height="14" viewBox="0 0 18 14"><path d="M1 7l5 5L17 1" fill="none" stroke="var(--green)" stroke-width="3"/></svg>Brigade of Sweepers is super flexible and affordable.</li>
    <li><svg width="18" height="14" viewBox="0 0 18 14"><path d="M1 7l5 5L17 1" fill="none" stroke="var(--green)" stroke-width="3"/></svg>Backed by our unique 200% Guarantee. You have nothing to lose.</li>
  </ul>

  <form class="quote-form">
    <h2>Get a Price</h2>
    <div class="field">Zip Code</div>
    <div class="label">Cleaning Style</div>
    <div class="toggle"><span class="on">Flat Rate</span><span>Hourly</span></div>
    <div class="label">Tell us about your home</div>
    <div class="stepper"><span class="btn">-</span><span class="val">2 bedrooms</span><span class="btn">+</span></div>
    <div class="hint">(living room &amp; kitchen included)</div>
    <div class="stepper"><span class="btn">-</span><span class="val">1 bathroom</span><span class="btn">+</span></div>
    <div class="hint">(round half baths up)</div>
    <div class="label">When would you like us to come?</div>
    <div class="field" style="color:#444;margin-bottom:12px">12/28/2016</div>
    <div class="label">Any time between</div>
    <div class="times"><span class="field">9:00 AM</span>and<span class="field">8:00 AM</span></div>
    <div class="flex-check"><i>✓</i>I'm flexible</div>
    <div class="cta">Get a Price</div>
  </form>
</section>

<section class="about">
  <h2 class="section-title">Who we are?</h2>
  <p class="intro">First and foremost, Brigade of Sweepers provides world class customer service. We don't just say that either. We want to WOW every single customer and leave them with a smile. We want to impress you so much that you invite us over for Thanksgiving dinner :).</p>
  <div class="circles">
    <div class="circle" role="img" aria-label="Maid vacuuming a living room" style="left:150px;background:radial-gradient(circle,#b9a48c,#6d5d4e)"></div>
    <div class="circle" role="img" aria-label="Maid wiping a framed picture" style="left:502px;background:radial-gradient(circle,#c9c1b4,#7f7466)"></div>
    <div class="circle" role="img" aria-label="Cleaning team at a client's front door" style="left:860px;background:radial-gradient(circle,#8a97a6,#3e4c5d)"></div>
  </div>
  <p class="contact">Need to contact us? No problem. You can reach us 24/7 via chat, email, or phone. Need to book some awesome maid service? We got your back. We can do that for you or you can take advantage of how simple and easy we made it to book online.</p>
  <span class="learn">Learn more &gt;&gt;</span>
</section>

<section class="reviews">
  <h2 class="section-title">A word from our customers</h2>
  <p class="sub">97% of our customers would recommend our maid services to friends &amp; family.</p>
  <div class="review" style="left:59px"><q>I love your company! You did such a great job cleaning my house. Thanks for working with me on the time crunch! The party went off without a hitch !</q><div class="who">MARLA</div><div class="stars"><span></span><span></span><span></span><span></span><span></span></div></div>
  <div class="review" style="left:460px"><q>Devon, I just wanted to thank you for your help in getting my house ready for showing! Within a week of your team cleaning it well, I got an excellent offer and will be closing on the sale in 2 weeks!! You guys are the best!! Thank you!</q><div class="who">RENATA BELL-KOVAC</div><div class="stars"><span></span><span></span><span></span><span></span><span></span></div></div>
  <div class="review" style="left:863px"><q>Lorem ipsum dolor sit amet, consectetuer adipiscing elit. Aenean commodo ligula eget dolor. Aenean massa. Cum sociis natoque penatibus et magnis dis parturient montes, nascetur ridiculus mus!</q><div class="who">ANONYMOUS</div><div class="stars"><span></span><span></span><span></span><span></span><span></span></div></div>
</section>

<section class="services">
  <h2 class="section-title">Comprehensive and consistent home cleaning. Every Time.</h2>
  <div class="tile" style="left:106px"><div class="shot" role="img" aria-label="Maid tidying a child's bedroom" style="background:linear-gradient(135deg,#6a5346,#a0685a)"></div><p>Bedrooms &amp; Common Areas</p></div>
  <div class="tile" style="left:460px"><div class="shot" role="img" aria-label="Maid cleaning a bathroom vanity" style="background:linear-gradient(135deg,#d8c9b0,#9c8f7c)"></div><p>Bathrooms</p></div>
  <div class="tile" style="left:820px"><div class="shot" role="img" aria-label="Maid dusting a computer desk" style="background:linear-gradient(135deg,#6fa37b,#3b4a52)"></div><p>Extras</p></div>
  <p class="note">Have explicit home cleaning requests? We're happy to accommodate you! Just let us know your scheduling.</p>
</section>

<section class="area">
  <div class="area-bg" role="img" aria-label="Branded company car parked outside a home, tinted blue"></div>
  <h2 class="section-title">Our Service Area - Meet our local cleaning pro at your  house</h2>
  <ul class="cities" style="left:74px"><li>Orlando</li><li>Winter Park</li><li>Winter Garden</li><li>Maitland</li><li>Apopka</li></ul>
  <ul class="cities" style="left:354px"><li>Edgewood</li><li>Ocoee</li><li>Belle Isle</li><li>Bay Lake,</li><li>Lake Buena Vista</li></ul>
  <ul class="cities" style="left:650px"><li>Oakland</li><li>Windermere</li><li>Sanford</li><li>Altamonte Springs</li><li>Casselberry</li></ul>
  <ul class="cities" style="left:936px"><li>Lake Mary</li><li>Longwood</li><li>Oviedo</li><li>Winter Springs</li></ul>
  <span class="schedule">Schedule Now</span>
</section>

<section class="press">
  <h2 class="section-title">Our Featured Publications</h2>
  <div class="outlets"><span>Lakeside Courier</span><span>Central Weekly</span><span>pure &amp; green</span><span>bluestone</span></div>
</section>

<footer class="site-footer">
  <div class="foot-brand"><span class="brand-dot"></span><span class="brand-name">Brigade of Sweepers</span></div>
  <p class="copy">© Copyright Brigade of Sweepers 2013</p>
  <ul class="foot-links" style="left:464px"><li>FAQ</li><li>Blog</li><li>Jobs</li></ul>
  <ul class="foot-links" style="left:638px"><li>Terms of Service</li><li>Privacy Policy</li><li>Sitemap</li></ul>
  <div class="connect">
    <div>Connect with us:</div>
    <div class="icons"><span></span><span></span><span></span></div>
    <div>We accept:</div>
    <div class="cards"><span></span><span></span><span></span><span></span></div>
  </div>
</footer>

<div class="callbar">Call us now at (844) 555-0176</div>

</body>
</html>
```